Flyer Design Project

Business is Wexford In Home Care

We are an Australian provider of In Home Care services.

We have a focus on quality care and a high standard of service.

We are non medical

We want to promote the health, happiness and independence of senior citizens by providing some help at home for general domestic duties (cleaning, bed linnen), personal care (showering, grooming) and meal preparation etc.

Target Market(s)

Seniors (70+) and the Children of seniors.

Industry/Entity Type

Business

Requirements
Must have
• Colour scheme from our website (www.wexfordinhomecare.com.au) –

The uploaded Word doc contains the desired copy.

Leaflet will be a standard A4 size foldout with 6 panels, 3 on each side.

```html
<!DOCTYPE html>
<html lang="en">
<head>
<meta charset="utf-8">
<title>Wexford In Home Care – Flyer</title>
<link rel="stylesheet" href="https://fonts.googleapis.com/css2?family=Tinos:wght@400;700&family=Arimo:wght@400&display=swap">
<style>
  :root {
    --navy: #111f7c;
    --orange: #f7a31c;
    --orange-soft: #fcd58a;
    --cream: #fdf0dc;
    --white: #ffffff;
    --text: #1a237e;
    --photo-skin: #c9b8a6;
    --photo-dark: #1a1414;
    --photo-light: #e9e4df;
  }
  * { margin: 0; padding: 0; box-sizing: border-box; }
  html, body { width: 1200px; height: 864px; overflow: hidden; background: var(--white); }
  .flyer { position: relative; width: 1200px; height: 864px; overflow: hidden; font-family: "Arimo", Arial, sans-serif; color: var(--text); }

  .top-band { position: absolute; left: 0; top: 0; width: 1200px; height: 81px; background: var(--navy); }
  .brand-band { position: absolute; left: 0; top: 81px; width: 1200px; height: 74px;
    background: linear-gradient(90deg, var(--orange) 0%, var(--orange-soft) 45%, var(--cream) 75%, var(--white) 100%); }
  .brand { position: absolute; right: 42px; top: 93px; display: flex; align-items: center; gap: 14px; }
  .brand-mark { width: 40px; height: 40px; border-radius: 50%; background: var(--navy); }
  .brand-name { font-family: "Tinos", "Times New Roman", serif; font-weight: 400; font-size: 27px; color: var(--navy); }

  .photo-band { position: absolute; left: 0; top: 155px; width: 1200px; height: 288px; background: var(--navy); }
  .photo { position: absolute; box-shadow: 0 2px 6px rgba(0,0,0,.45); }
  .photo-carer { left: 36px; top: 170px; width: 352px; height: 251px;
    background: linear-gradient(120deg, var(--photo-light) 0%, #d8ccc0 45%, #b9c4c8 100%); }
  .photo-flower { left: 424px; top: 170px; width: 352px; height: 255px;
    background: radial-gradient(circle at 55% 55%, #b0307f 0%, #8a5a48 22%, var(--photo-dark) 60%); }
  .photo-companion { left: 811px; top: 170px; width: 351px; height: 255px;
    background: linear-gradient(110deg, #e8dfd4 0%, var(--photo-light) 50%, #f2efec 100%); }

  .content { position: absolute; left: 0; top: 443px; width: 1200px; height: 421px;
    background: linear-gradient(90deg, var(--orange) 0%, var(--orange-soft) 35%, var(--cream) 65%, var(--white) 100%); }

  .serif { font-family: "Tinos", "Times New Roman", serif; font-weight: 700; color: var(--navy); }
  .heading { position: absolute; font-size: 20px; line-height: 1; }

  .service-list { position: absolute; list-style: none; font-size: 14px; line-height: 20.7px; color: var(--navy); }
  .service-list li { position: relative; padding-left: 14px; }
  .service-list li::before { content: "•"; position: absolute; left: 0; }

  .panel-left .heading { left: 44px; top: 460px; }
  .panel-left .service-list { left: 44px; top: 502px; width: 336px; }
  .panel-left .slogan { left: 44px; top: 797px; }

  .panel-mid .heading { left: 420px; top: 459px; }
  .panel-mid .service-list { left: 420px; top: 501px; }
  .panel-mid .promise { left: 420px; top: 668px; }
  .panel-mid .call { left: 420px; top: 731px; }
  .contact { position: absolute; left: 420px; top: 758px; font-size: 13px; line-height: 20.5px; color: var(--navy); }
  .contact .web { font-family: "Tinos", "Times New Roman", serif; font-weight: 700; }

  .tagline { position: absolute; right: 43px; top: 454px; width: 380px; text-align: right; font-size: 25.5px; line-height: 37.5px; }
  .care-type { position: absolute; right: 43px; top: 713px; text-align: right; font-size: 16px; line-height: 23.7px; color: var(--navy); }
  .web-right { position: absolute; right: 43px; top: 796px; font-size: 14.5px; }
</style>
</head>
<body>
<main class="flyer">
  <div class="top-band"></div>
  <div class="brand-band"></div>
  <div class="brand">
    <span class="brand-mark"></span>
    <span class="brand-name">Wexford In Home Care</span>
  </div>

  <div class="photo-band"></div>
  <div class="photo photo-carer" role="img" aria-label="Photo of a smiling senior man with a carer's hand on his shoulder"></div>
  <div class="photo photo-flower" role="img" aria-label="Photo of cupped elderly hands holding a pink daisy"></div>
  <div class="photo photo-companion" role="img" aria-label="Photo of a young carer embracing a smiling elderly woman"></div>

  <div class="content"></div>

  <section class="panel-left">
    <h2 class="heading serif">Our Services</h2>
    <ul class="service-list">
      <li>Personal care- showering, dressing, hygiene and grooming</li>
      <li>Domestic Assistance- general cleaning, laundry, bed linen and ironing</li>
      <li>Meal Preparation- support to select, prepare and enjoy meals</li>
      <li>Respite- support for carers to take a well-earned break</li>
      <li>Companionship- visits, social outings, transport to appointments and support shopping</li>
      <li>Rehabilitation- support after surgery or recovering from illness</li>
    </ul>
    <p class="heading serif slogan">Reliable, compassionate, person centred</p>
  </section>

  <section class="panel-mid">
    <h2 class="heading serif">Our Services</h2>
    <ul class="service-list">
      <li>Personal Care</li>
      <li>Domestic Assistance</li>
      <li>Meal Preparation</li>
      <li>Respite</li>
      <li>Companionship</li>
      <li>Rehabilitation Support</li>
    </ul>
    <p class="heading serif promise">Providing Exceptional Care at home</p>
    <p class="heading serif call">Call 1300 555 014</p>
    <div class="contact">
      <p class="web">www.wexfordinhomecare.com.au</p>
      <p>contact@wexfordinhomecare.com.au</p>
      <p>Address: 12A/58 Harbour Lane Sydney NSW 2000</p>
    </div>
  </section>

  <section class="panel-right">
    <h1 class="tagline serif">In Home care specialists in the comfort and familiarity of your home.</h1>
    <p class="care-type">Professional<br>Non-medical<br>Companion based care</p>
    <p class="web-right serif">www.wexfordinhomecare.com.au</p>
  </section>
</main>
</body>
</html>
```